K&R Security Services PTY. LTD.

Ive just had my logo made and I'm looking for some simple but strong designs for my business cards the company is a security company.

Please use dark colors.

Regards,

Owen Deloit

Reason: Need more time for discussion with other directors

Industry/Entity Type

Security

Font styles to use
Sans Serif
Decorative

```html
<!DOCTYPE html>
<html lang="en">
<head>
<meta charset="utf-8">
<title>K&amp;R Security Services – Business Card</title>
<link rel="stylesheet" href="https://fonts.googleapis.com/css2?family=Fira+Sans+Condensed:wght@300;400&family=Fira+Sans:wght@400&display=swap">
<style>
  :root {
    --card-top: #4d4c4e;
    --card-back-left: #4a494b;
    --card-back-right: #666567;
    --band: #000000;
    --rule: #ffffff;
    --page: #ffffff;
    --name-ink: #111111;
    --role-ink: #363537;
    --band-ink: #ffffff;
    --mark-ink: #1c1b1d;
    --mark-tile: #2a292b;
  }
  * { margin: 0; padding: 0; box-sizing: border-box; }
  html, body {
    width: 1018px; height: 1200px; overflow: hidden;
    background: var(--page);
  }
  .canvas { position: relative; width: 1018px; height: 1200px; }

  /* Front of card */
  .card-front { position: absolute; left: 0; top: 0; width: 1018px; height: 582px; background: var(--card-top); }
  .identity { position: absolute; left: 78px; top: 146px; font-family: "Fira Sans Condensed", sans-serif; }
  .identity__name { font-weight: 400; font-size: 66px; line-height: 1; letter-spacing: 1px; color: var(--name-ink); }
  .identity__role { margin: 4px 0 0 82px; font-weight: 400; font-size: 37px; line-height: 1; letter-spacing: 1px; color: var(--role-ink); }

  .brand { position: absolute; display: flex; align-items: center; gap: 14px; font-family: "Fira Sans Condensed", sans-serif; font-weight: 400; color: var(--mark-ink); white-space: nowrap; }
  .brand__tile { background: var(--mark-tile); }
  .brand--front { left: 640px; top: 200px; font-size: 46px; }
  .brand--front .brand__tile { width: 40px; height: 40px; }

  .contact-band {
    position: absolute; left: 0; top: 407px; width: 1018px; height: 175px;
    background: var(--band); border-top: 4px solid var(--rule);
    font-family: "Fira Sans", sans-serif; color: var(--band-ink);
  }
  .contact-list { position: absolute; left: 32px; top: 20px; list-style: none; }
  .contact-list li { display: flex; align-items: baseline; height: 46px; }
  .contact-list__label { width: 111px; font-size: 22px; }
  .contact-list__value { font-size: 32px; letter-spacing: 0.5px; }
  .web { position: absolute; right: 30px; top: 64px; text-align: right; }
  .web__site { font-size: 30px; letter-spacing: 1px; }
  .web__email { margin-top: 14px; font-size: 22px; letter-spacing: 1px; }

  /* Back of card */
  .card-back {
    position: absolute; left: 0; top: 618px; width: 1018px; height: 582px;
    background: linear-gradient(to right, var(--card-back-left) 50%, var(--card-back-right) 50%);
  }
  .brand--back { left: 50%; top: 50%; transform: translate(-50%, -50%); font-size: 64px; }
  .brand--back .brand__tile { width: 54px; height: 54px; }
</style>
</head>
<body>
<main class="canvas">
  <section class="card-front">
    <div class="identity">
      <h1 class="identity__name">OWEN DELOIT</h1>
      <p class="identity__role">PRIVATE SECURITY</p>
    </div>
    <div class="brand brand--front"><span class="brand__tile"></span><span>K&amp;R SECURITY</span></div>
    <div class="contact-band">
      <ul class="contact-list">
        <li><span class="contact-list__label">PHONE</span><span class="contact-list__value">(00) 0000 0000</span></li>
        <li><span class="contact-list__label">FAX</span><span class="contact-list__value">(00) 0000 0000</span></li>
        <li><span class="contact-list__label">MOBILE</span><span class="contact-list__value">(00) 0000 0000</span></li>
      </ul>
      <div class="web">
        <p class="web__site">WWW.WEBSITE.COM.AU</p>
        <p class="web__email">EMAIL@WWW.WEBSITE.COM.AU</p>
      </div>
    </div>
  </section>
  <section class="card-back">
    <div class="brand brand--back"><span class="brand__tile"></span><span>K&amp;R SECURITY</span></div>
  </section>
</main>
</body>
</html>
```